Business Card for Managing Partner Investment Fund

To create a business card template for an investment fund manager. Business card should be more professional in nature, not too colorful, more upscale, and created using the attached logos and fund name files. I would prefer a black or gray color scheme, but am open to the use of color as well. I would prefer a double sided business card, but open to single sided business card designs as well. The business card should include: name, title, and contact information, as well as logo and company name. I would prefer a more stream-lined, simple business card design.
Updates
Address: 4190 NE 38th Ter. Ocala, FL 34470
Email: talvin47@quorimail.net
Phone: 561-347-9162
Title: managing partner
Name: Dorian Velsky
Fund Name: Ambergate Capital
Logos can be found in files attached to the brief
Target Market(s)
potential investors, other fund managers
Industry/Entity Type
Finance
Contact Information for Business Card
Name on card: Dorian Velsky
Title: Managing Partner
Colors
Designer to choose colors to be used in the design.
Requirements
Must have
- Phone number
- email address
- physical address
- title
- name
- logo
- Fund name
Nice to have
- simple layout
Should not have
- too many colors, busy fonts,

```html
<!DOCTYPE html>
<html lang="en">
<head>
<meta charset="utf-8">
<title>Ambergate Capital – Business Card</title>
<link href="https://fonts.googleapis.com/css2?family=Cinzel:wght@400;600&family=Nunito+Sans:wght@400&display=swap" rel="stylesheet">
<style>
  :root {
    --backdrop: #2b2b2b;
    --card: #050505;
    --silver: #c9c9c9;
    --grey: #8a8a8a;
    --white: #ececec;
    --rule: #7a7a7a;
  }
  * { box-sizing: border-box; margin: 0; padding: 0; }
  html, body {
    width: 1200px; height: 900px; overflow: hidden;
    background: var(--backdrop);
  }
  .sheet { position: relative; width: 1200px; height: 900px; }
  .card {
    position: absolute; left: 250px;
    width: 700px; height: 400px;
    background: var(--card);
    box-shadow: 0 12px 30px rgba(0,0,0,.55);
    overflow: hidden;
  }
  .card-front { top: 40px; }
  .card-back { top: 460px; }

  .wordmark {
    font-family: "Cinzel", serif;
    font-weight: 600;
    letter-spacing: 2px;
    text-transform: uppercase;
    text-align: center;
    line-height: 1.15;
  }
  .card-front .wordmark {
    position: absolute; left: 120px; top: 145px; width: 300px;
    color: var(--silver); font-size: 40px;
  }
  .card-back .wordmark {
    position: absolute; left: 70px; top: 160px; width: 260px;
    color: var(--grey); font-size: 32px;
  }

  .divider {
    position: absolute; left: 355px; top: 110px;
    width: 1px; height: 180px; background: var(--rule);
  }
  .contact {
    position: absolute; left: 375px; top: 112px;
    font-family: "Nunito Sans", sans-serif;
    color: var(--grey);
  }
  .contact-name {
    font-family: "Cinzel", serif; font-weight: 400;
    font-size: 20px; letter-spacing: 1px; text-transform: uppercase;
    color: var(--grey);
  }
  .contact-title { font-size: 16px; color: var(--white); margin-bottom: 14px; }
  .contact-list { list-style: none; }
  .contact-item {
    display: flex; align-items: center; gap: 10px;
    font-size: 15px; margin-bottom: 8px;
  }
  .contact-icon { width: 14px; height: 14px; fill: var(--white); flex: none; }
</style>
</head>
<body>
<main class="sheet">
  <section class="card card-front">
    <div class="wordmark">Ambergate<br>Capital</div>
  </section>

  <section class="card card-back">
    <div class="wordmark">Ambergate<br>Capital</div>
    <div class="divider"></div>
    <div class="contact">
      <div class="contact-name">Dorian Velsky</div>
      <div class="contact-title">Managing Partner</div>
      <ul class="contact-list">
        <li class="contact-item">
          <svg class="contact-icon" viewBox="0 0 24 24"><path d="M6.6 10.8a15.2 15.2 0 0 0 6.6 6.6l2.2-2.2a1 1 0 0 1 1-.25 11.4 11.4 0 0 0 3.6.57 1 1 0 0 1 1 1V20a1 1 0 0 1-1 1A17 17 0 0 1 3 4a1 1 0 0 1 1-1h3.5a1 1 0 0 1 1 1c0 1.25.2 2.45.57 3.57a1 1 0 0 1-.25 1z"/></svg>
          <span>561-347-9162</span>
        </li>
        <li class="contact-item">
          <svg class="contact-icon" viewBox="0 0 24 24"><path d="M2 5h20v14H2z M3.5 6.5 12 13l8.5-6.5" fill="var(--white)" stroke="var(--card)" stroke-width="1.5"/></svg>
          <span>talvin47@quorimail.net</span>
        </li>
        <li class="contact-item">
          <svg class="contact-icon" viewBox="0 0 24 24"><path d="M12 3 2 12h3v8h5v-5h4v5h5v-8h3z"/></svg>
          <span>4190 NE 38th Ter. Ocala, FL 34470</span>
        </li>
      </ul>
    </div>
  </section>
</main>
</body>
</html>
```